IT Services Company - Company Logo, Flyer design

We are an IT professional services company that provides technical service and support in the residential market. I would like to create a colorful logo and flyer that will be mainly letterbox dropped.

Target Market(s)

residential

Industry/Entity Type

It Company

Requirements
Must have
• nice look and feel, easy to read

```html
<!DOCTYPE html>
<html lang="en">
<head>
<meta charset="utf-8">
<title>Nexalink Tech – Home Technology Services</title>
<link href="https://fonts.googleapis.com/css2?family=Oswald:wght@500&family=Lato:ital,wght@0,400;0,700;1,700&display=swap" rel="stylesheet">
<style>
:root{
  --blue:#1a6fba;
  --blue-dark:#135d9f;
  --orange:#e8501b;
  --ink:#1e1e1e;
  --line:#8a8f96;
  --page:#f2f2f0;
  --paper:#ffffff;
}
*{box-sizing:border-box;margin:0;padding:0}
html,body{width:1200px;height:1200px;overflow:hidden;background:var(--page)}
.flyer{position:absolute;left:172px;top:0;width:856px;height:1200px;background:var(--paper);overflow:hidden;font-family:'Lato',sans-serif;color:var(--ink)}
.hero{position:absolute;left:0;top:0;width:856px;height:415px}
.brand{position:absolute;left:540px;top:78px;display:flex;align-items:center;gap:10px}
.brand-dot{width:26px;height:26px;border-radius:50%;background:var(--orange)}
.brand-name{font-family:'Oswald',sans-serif;font-weight:500;font-size:40px;color:var(--blue);letter-spacing:1px;line-height:1}
.hero-title{position:absolute;right:53px;top:214px;font-family:'Oswald',sans-serif;font-weight:500;font-size:27px;letter-spacing:-.3px;color:var(--blue);white-space:nowrap}
.hero-title .hl{color:var(--orange)}
.hero-copy{position:absolute;right:53px;top:268px;text-align:right;font-weight:700;line-height:26.5px}
.hero-copy .dark{color:var(--ink);font-size:21px}
.hero-copy .blue{color:var(--blue);font-size:20px}
.hero-copy .orange{color:var(--orange);font-size:22px}
.intro{position:absolute;left:53px;top:452px}
.intro h1{font-family:'Oswald',sans-serif;font-weight:500;font-size:29px;line-height:40px;color:var(--blue);letter-spacing:-.2px}
.intro p{margin-top:18px;font-style:italic;font-weight:700;font-size:24px;line-height:30px;color:var(--blue)}
.intro p .hl{color:var(--orange)}
.service{position:absolute;border:1.5px solid var(--line);border-radius:9px;padding:14px 14px 0 18px;background:var(--paper)}
.service h2{display:flex;align-items:center;gap:12px;font-family:'Oswald',sans-serif;font-weight:500;font-size:20px;color:var(--blue);letter-spacing:-.2px;line-height:24px}
.service h2 svg{flex:none}
.service ul{list-style:none;margin-top:10px}
.service li{display:flex;gap:16px;font-size:17.5px;line-height:21px;white-space:nowrap}
.service li svg{flex:none;margin-top:3px}
.box-computers{left:442px;top:447px;width:363px;height:189px}
.box-email{left:48px;top:655px;width:362px;height:202px}
.box-internet{left:442px;top:655px;width:363px;height:202px}
.box-tv{left:48px;top:875px;width:362px;height:225px}
.box-tv ul{margin-top:8px}
.box-tv li{line-height:20.5px}
.box-phones{left:442px;top:875px;width:363px;height:107px}
.box-printers{left:442px;top:999px;width:215px;height:101px;padding-left:16px;padding-right:6px}
.experience{position:absolute;left:672px;top:1004px;width:126px;text-align:center;font-family:'Oswald',sans-serif;font-weight:500;line-height:.98}
.experience .over{font-size:38px;color:var(--blue);letter-spacing:1px}
.experience .years{font-size:29px;color:var(--orange)}
.experience .exp{font-size:29px;color:var(--blue)}
.footer{position:absolute;left:0;bottom:0;width:856px;height:90px;background:var(--blue)}
.footer-accent{position:absolute;left:0;top:0}
.contacts{position:absolute;left:28px;top:34px;display:flex;align-items:center;gap:26px;color:#fff;font-size:19px}
.contacts span{display:flex;align-items:center;gap:10px}
</style>
</head>
<body>
<div class="flyer">
  <svg class="hero" viewBox="0 0 856 415" width="856" height="415">
    <defs>
      <linearGradient id="photoTone" x1="0" y1="0" x2="1" y2="1">
        <stop offset="0" stop-color="#3c4b5c"/>
        <stop offset=".45" stop-color="#aeb9c4"/>
        <stop offset=".75" stop-color="#6f7a86"/>
        <stop offset="1" stop-color="#2a2f36"/>
      </linearGradient>
      <linearGradient id="panelTone" x1="0" y1="0" x2="0" y2="1">
        <stop offset="0" stop-color="#ffffff"/>
        <stop offset="1" stop-color="#e3e4e6"/>
      </linearGradient>
    </defs>
    <rect width="856" height="415" fill="#fff"/>
    <polygon points="0,0 545,0 421,415 0,415" fill="url(#photoTone)" role="img" aria-label="Photo: businessman's open hand presenting glowing cloud, device and network icons in a server room"/>
    <polygon points="496,184 856,184 856,396 433,396" fill="url(#panelTone)"/>
    <line x1="496" y1="184" x2="856" y2="184" stroke="#1a6fba" stroke-width="1.5"/>
    <polygon points="433,396 856,396 856,415 427,415" fill="#e8501b"/>
    <polygon points="545,0 556,0 432,415 421,415" fill="#1a6fba"/>
  </svg>

  <div class="brand"><span class="brand-dot"></span><span class="brand-name">Nexalink Tech</span></div>

  <div class="hero-title"><span class="hl">HOME TECHNOLOGY</span> SERVICES</div>
  <div class="hero-copy">
    <div class="dark">Professional and reliable</div>
    <div class="blue">IT SERVICE COMPANY</div>
    <div class="orange">HELPING WITH ALL YOUR</div>
    <div class="blue">HOME TECHNOLOGY NEEDS</div>
  </div>

  <div class="intro">
    <h1>TECHNOLOGY PROCUREMENT,<br>SETUP, SERVICE AND TRAINING</h1>
    <p><span class="hl">Competitive rates,</span> obligation<br>free quotes, no job too small</p>
  </div>

  <section class="service box-computers">
    <h2><svg width="22" height="20" viewBox="0 0 22 20"><rect width="22" height="20" rx="2" fill="#1a6fba"/><rect x="4" y="4" width="14" height="9" fill="none" stroke="#fff" stroke-width="1.6"/><line x1="8" y1="16" x2="14" y2="16" stroke="#fff" stroke-width="1.6"/></svg>COMPUTERS AND DATA BACKUP</h2>
    <ul>
      <li><svg width="16" height="14"><rect x="1" y="1" width="14" height="9" fill="none" stroke="#e8501b" stroke-width="1.5"/><line x1="5" y1="13" x2="11" y2="13" stroke="#e8501b" stroke-width="1.5"/></svg>New computer set up</li>
      <li><svg width="16" height="14"><rect x="5" y="1" width="10" height="8" fill="none" stroke="#e8501b" stroke-width="1.5"/><circle cx="3" cy="6" r="2" fill="#e8501b"/><line x1="3" y1="8" x2="3" y2="14" stroke="#e8501b" stroke-width="2"/></svg>Training</li>
      <li><svg width="16" height="14"><path d="M2 12 A6 6 0 1 1 14 12" fill="none" stroke="#e8501b" stroke-width="1.5"/><line x1="8" y1="11" x2="11" y2="6" stroke="#e8501b" stroke-width="1.5"/></svg>Improve performance</li>
      <li><svg width="16" height="14"><rect x="2" y="1" width="12" height="9" fill="none" stroke="#e8501b" stroke-width="1.5"/><circle cx="8" cy="5.5" r="2" fill="#e8501b"/><line x1="5" y1="13" x2="11" y2="13" stroke="#e8501b" stroke-width="1.5"/></svg>Virus removal</li>
      <li><svg width="18" height="14"><path d="M4 12 H14 A3.5 3.5 0 0 0 13 5 A5 5 0 0 0 4 6 A3 3 0 0 0 4 12Z" fill="none" stroke="#e8501b" stroke-width="1.5"/><path d="M9 11 V7 M7 9 L9 7 L11 9" fill="none" stroke="#e8501b" stroke-width="1.3"/></svg>Local and cloud backup solutions<br>(eg. SkyVault)</li>
    </ul>
  </section>

  <section class="service box-email">
    <h2><svg width="22" height="20" viewBox="0 0 22 20"><rect width="22" height="20" rx="2" fill="#1a6fba"/><rect x="4" y="6" width="14" height="9" fill="none" stroke="#fff" stroke-width="1.6"/><path d="M4 6 L11 11 L18 6" fill="none" stroke="#fff" stroke-width="1.6"/></svg>EMAIL</h2>
    <ul>
      <li><svg width="16" height="14"><rect x="1" y="4" width="14" height="9" fill="#e8501b"/><path d="M1 4 L8 9 L15 4" fill="none" stroke="#fff" stroke-width="1.3"/></svg>New email set up</li>
      <li><svg width="16" height="14"><circle cx="8" cy="7" r="6" fill="none" stroke="#e8501b" stroke-width="1.5"/><circle cx="8" cy="7" r="2" fill="#e8501b"/></svg>Domain set up and email migration<br>to cloud provider</li>
      <li><svg width="16" height="14"><rect x="1" y="2" width="12" height="9" fill="none" stroke="#e8501b" stroke-width="1.3"/><path d="M1 2 L7 7 L13 2" fill="none" stroke="#e8501b" stroke-width="1.3"/></svg>Linking new email account to<br>multiple devices</li>
      <li><svg width="16" height="14"><rect x="5" y="1" width="10" height="8" fill="none" stroke="#e8501b" stroke-width="1.5"/><circle cx="3" cy="6" r="2" fill="#e8501b"/><line x1="3" y1="8" x2="3" y2="14" stroke="#e8501b" stroke-width="2"/></svg>Training</li>
    </ul>
  </section>

  <section class="service box-internet">
    <h2><svg width="22" height="20" viewBox="0 0 22 20"><rect width="22" height="20" rx="2" fill="#1a6fba"/><circle cx="11" cy="10" r="6" fill="none" stroke="#fff" stroke-width="1.6"/><line x1="5" y1="10" x2="17" y2="10" stroke="#fff" stroke-width="1.2"/></svg>INTERNET / WIFI</h2>
    <ul>
      <li><svg width="16" height="14"><path d="M1 6 A10 10 0 0 1 15 6 M4 9 A6 6 0 0 1 12 9" fill="none" stroke="#e8501b" stroke-width="1.5"/><circle cx="8" cy="12" r="1.6" fill="#e8501b"/></svg>Wireless and home network set up</li>
      <li><svg width="16" height="14"><path d="M1 6 A10 10 0 0 1 15 6 M4 9 A6 6 0 0 1 12 9" fill="none" stroke="#e8501b" stroke-width="1.2"/><circle cx="8" cy="12" r="1.6" fill="none" stroke="#e8501b"/></svg>Extend and improve existing home<br>wireless</li>
      <li><svg width="16" height="14"><path d="M2 4 H12 L9 1 M14 10 H4 L7 13" fill="none" stroke="#e8501b" stroke-width="1.5"/></svg>Improve slow connections</li>
      <li><svg width="16" height="14"><path d="M8 1 L14 3 V7 C14 10 11 12 8 13 C5 12 2 10 2 7 V3Z" fill="#e8501b"/></svg>Security</li>
      <li><svg width="16" height="14"><rect x="5" y="1" width="10" height="8" fill="none" stroke="#e8501b" stroke-width="1.5"/><circle cx="3" cy="6" r="2" fill="#e8501b"/><line x1="3" y1="8" x2="3" y2="14" stroke="#e8501b" stroke-width="2"/></svg>Training</li>
    </ul>
  </section>

  <section class="service box-tv">
    <h2><svg width="22" height="20" viewBox="0 0 22 20"><rect x="1" y="4" width="20" height="15" rx="1" fill="none" stroke="#1a6fba" stroke-width="2"/><path d="M7 0 L11 4 L15 0" fill="none" stroke="#1a6fba" stroke-width="1.6"/></svg>TV'S / SPEAKERS AND CAMERAS</h2>
    <ul>
      <li><svg width="16" height="14"><rect x="1" y="3" width="14" height="10" rx="2" fill="#e8501b"/><path d="M5 0 L8 3 L11 0" fill="none" stroke="#e8501b" stroke-width="1.3"/></svg>New TV set up</li>
      <li><svg width="16" height="14"><rect x="1" y="1" width="14" height="9" fill="none" stroke="#e8501b" stroke-width="1.3"/><path d="M6 3 L10 5.5 L6 8Z" fill="#e8501b"/><line x1="5" y1="13" x2="11" y2="13" stroke="#e8501b" stroke-width="1.3"/></svg>Set up streaming services (eg. Flixa)</li>
      <li><svg width="16" height="14"><circle cx="8" cy="7" r="5.5" fill="none" stroke="#e8501b" stroke-width="3" stroke-dasharray="3 1.5"/><circle cx="8" cy="7" r="2" fill="#e8501b"/></svg>Set up linked devices (eg. CastLink,<br>Orchard TV)</li>
      <li><svg width="16" height="14"><path d="M1 5 H4 L9 1 V13 L4 9 H1Z" fill="#e8501b"/><path d="M11 4 A4 4 0 0 1 11 10" fill="none" stroke="#e8501b" stroke-width="1.3"/></svg>Auralis speaker set up (Music<br>streaming eg. TuneWave).</li>
      <li><svg width="16" height="14"><circle cx="8" cy="7" r="6" fill="#e8501b"/><circle cx="8" cy="7" r="2.5" fill="#fff"/></svg>Camera installations - internal and<br>external</li>
    </ul>
  </section>

  <section class="service box-phones">
    <h2><svg width="22" height="20" viewBox="0 0 22 20"><rect width="22" height="20" rx="2" fill="#1a6fba"/><rect x="4" y="4" width="5" height="12" fill="#fff"/><rect x="11" y="4" width="7" height="12" fill="none" stroke="#fff" stroke-width="1.4"/></svg>MOBILE AND LANDLINE PHONES</h2>
    <ul>
      <li><svg width="16" height="14"><rect x="3" y="0" width="9" height="14" rx="1.5" fill="none" stroke="#e8501b" stroke-width="1.5"/><circle cx="7.5" cy="11" r="1" fill="#e8501b"/></svg>New phone set up</li>
      <li><svg width="16" height="14"><rect x="5" y="1" width="10" height="8" fill="none" stroke="#e8501b" stroke-width="1.5"/><circle cx="3" cy="6" r="2" fill="#e8501b"/><line x1="3" y1="8" x2="3" y2="14" stroke="#e8501b" stroke-width="2"/></svg>Training</li>
    </ul>
  </section>

  <section class="service box-printers">
    <h2><svg width="22" height="20" viewBox="0 0 22 20"><rect x="5" y="1" width="12" height="5" fill="#1a6fba"/><rect x="1" y="7" width="20" height="8" rx="1" fill="#1a6fba"/><rect x="5" y="12" width="12" height="7" fill="#fff" stroke="#1a6fba" stroke-width="1.5"/></svg>PRINTERS</h2>
    <ul>
      <li><svg width="16" height="14"><rect x="4" y="1" width="8" height="4" fill="none" stroke="#e8501b" stroke-width="1.2"/><rect x="1" y="5" width="14" height="6" fill="none" stroke="#e8501b" stroke-width="1.2"/><rect x="4" y="9" width="8" height="4" fill="#fff" stroke="#e8501b" stroke-width="1.2"/></svg>New printer set up</li>
      <li><svg width="16" height="14"><rect x="2" y="1" width="11" height="12" fill="none" stroke="#e8501b" stroke-width="1.2"/><path d="M5 4 L10 10 M10 4 L5 10" stroke="#e8501b" stroke-width="1.2"/></svg>Troubleshooting</li>
    </ul>
  </section>

  <div class="experience">
    <div class="over">OVER</div>
    <div class="years">15 YEARS</div>
    <div class="exp">EXPERIENCE</div>
  </div>

  <footer class="footer">
    <svg class="footer-accent" width="856" height="10" viewBox="0 0 856 10"><polygon points="408,0 856,0 856,10 418,10" fill="#e8501b"/></svg>
    <div class="contacts">
      <span><svg width="30" height="22" viewBox="0 0 30 22"><rect x="1" y="1" width="7" height="20" rx="1" fill="#fff"/><rect x="10" y="1" width="19" height="20" rx="1" fill="none" stroke="#fff" stroke-width="2"/><path d="M14 6 H25 M14 11 H25 M14 16 H25" stroke="#fff" stroke-width="2" stroke-dasharray="2 2"/></svg>(02) 5550 1234</span>
      <span><svg width="24" height="24" viewBox="0 0 24 24"><circle cx="12" cy="12" r="10.5" fill="#fff"/><path d="M6 7 C9 8 10 6 12 9 C13 12 9 12 10 16 M15 5 C17 9 19 9 19 13 C17 15 15 14 15 18" fill="none" stroke="#1a6fba" stroke-width="2"/></svg>nexalinktech.com.au</span>
      <span><svg width="26" height="24" viewBox="0 0 26 24"><path d="M2 10 L13 2 L24 10 V22 H2Z" fill="#fff"/><path d="M2 10 L13 17 L24 10" fill="none" stroke="#1a6fba" stroke-width="1.6"/></svg>help@nexalinktech.com.au</span>
    </div>
  </footer>
</div>
</body>
</html>
```